Packaging Design Project For Chocolate Brand

We need a fresh, vibrant and colourful packaging for our healthy chocolate brand, oTakeFernubrio.

WHAT IS oTakeFernubrio?

oTakeFernubrio are indulgent chocolates that help reduce your body weight by controlling your appetite and calorie intake. And the best thing is that it tastes 100% genuine chocolate, only healthier.

WHAT WE NEED FROM YOU

Although we have collected a few logos from other designers, it's not quite catchy to the eye. As it will appear on retail shelves, it needs to catch the eye. It's up to the designers if they want to design the logo all in one word or two words. We will provide feedback quickly. We are contemplating on a sub-title beneath the logo, with the words "Unwrap. Eat. Lose." It is the main logo "oTakeFernubrio" that needs to stand out though with possibly some chocolatey or slimming/dieting aspect. However we do not want any images of thin bodies around the logo. Use of imagination involving chocolate could be beneficial, e.g. melting chocolate etc.
Use different colours for 'i', 'Love', and 'Fernubrio'. Maybe include an illustration around the logo if you feel it will brighten the brand.

Packaging

Although we do not have a specific theme in mind, the designer may want to try a retro look with illustrations/images, funky, maybe professional but keep it modern and looking like a chocolate bar.

Dimensions - 155mm(width) x 76.8mm(height) x 34mm(depth)
Portrait or landscape. Designers choice.

There are three flavours, Milk, White and Dark so three different packages with different colours. The rest of the packages will look more or less the same. The packaging itself needs 'wavey' aspects of chocolate. Wavey, circular, elegant shapes which appeal to the eye

There are certain texts which need to go on the front end of the box. The designer has the option of using 2 different texts in their work to come up with the best design. Texts are on the files. More text may be added but in the meantime please use what is given.
Updates

Project Deadline Extended
Reason: Hi, The deadline has been extended a further 7 days for those who designers who started their designs late are concerned about the timeframe. So there is no need to rush your designs. I hope the 7 days extension is enough for those that need it. Many thanks,

Target Market(s)

Women aged 16-45, C1C2 class

Industry/Entity Type

Landscape

Requirements
Must have
• Appealing mostly to women aged 16-45, C1C2 class.
Colourful
Chocolatey feel with wavey lines etc
Strong Logo
Nice to have
• It can come across as a food supplement that you normally see on the pharmacy shelf but with an unconventional design twist. Or the designer may think it will not work and for it to have the chocolatey feel, there cannot be any connection a pharmaceutical package. It has to remain like a regular chocolate bar that you see in the supermarket. Up to the designer to choose. It will be going into both supermarket stores and healthfood stores.

The designer should have some personal input in the design. If you were browsing around the supermarket and spotted it, would you stop and look at it? If not, the design will need changing.

Secondly, maybe a brand illustration would go well with the logo. Possibly an animal illustration relating to chocolate (somehow) or simply a chocolate with a measuring tape around it getting slimmer and slimmer. Just a few thoughts

```html
<!DOCTYPE html>
<html lang="en">
<head>
<meta charset="utf-8">
<title>oTakeFernubrio – Chocolate Box Range</title>
<link rel="stylesheet" href="https://fonts.googleapis.com/css2?family=Jost:wght@400;500&display=swap">
<style>
  :root {
    --page: #ffffff;
    --frame: #ffffff;
    --cocoa: #563427;
    --milk: #7e4f3d;
    --dark: #2b0f0a;
    --white-choc: #ffffff;
    --pink: #e9008a;
    --ink-light: #ffffff;
    --ink-dark: #3a1a12;
    --brand-ink: #3a1a12;
  }
  html, body {
    margin: 0;
    padding: 0;
    width: 1200px;
    height: 1097px;
    overflow: hidden;
    background: var(--page);
  }
  .range {
    position: relative;
    width: 1200px;
    height: 1097px;
    font-family: "Jost", "Futura", sans-serif;
  }
  .box-front {
    position: absolute;
    width: 776px;
    height: 386px;
    filter: drop-shadow(1px 2px 3px rgba(0,0,0,0.35));
  }
  .box-front--dark  { left: 330px; top: 115px; z-index: 1; }
  .box-front--white { left: 218px; top: 344px; z-index: 2; }
  .box-front--milk  { left: 107px; top: 571px; z-index: 3; }

  .frame { fill: var(--frame); }
  .panel { fill: var(--cocoa); }
  .brand-block { fill: var(--pink); }
  .brand-dot { fill: var(--brand-ink); }
  .brand-name { fill: var(--brand-ink); font-size: 30px; font-weight: 500; letter-spacing: 2px; }
  .flavour-tab--dark  { fill: var(--dark); }
  .flavour-tab--white { fill: var(--white-choc); }
  .flavour-tab--milk  { fill: var(--milk); }
  .flavour-name { font-size: 33px; font-weight: 400; }
  .flavour-name--light { fill: var(--ink-light); }
  .flavour-name--dark  { fill: var(--ink-dark); }
  .weight-tab { fill: var(--milk); }
  .copy { fill: var(--ink-light); font-size: 21px; }
  .net-weight { fill: var(--ink-light); font-size: 20px; }
</style>
</head>
<body>
<main class="range">

  <svg class="box-front box-front--dark" viewBox="0 0 776 386" aria-label="Dark box front">
    <rect class="frame" width="776" height="386"/>
    <rect class="panel" x="3" y="3" width="770" height="380"/>
    <rect class="brand-block" x="3" y="3" width="405" height="177"/>
    <circle class="brand-dot" cx="44" cy="96" r="9"/>
    <text class="brand-name" x="64" y="107" textLength="310" lengthAdjust="spacing">OTAKEFERNUBRIO</text>
    <polygon class="flavour-tab--dark" points="448,3 773,3 773,100 463,135"/>
    <text class="flavour-name flavour-name--light" x="738" y="66" text-anchor="end" textLength="253" lengthAdjust="spacingAndGlyphs">Dark Box - Daily Fix</text>
    <text class="copy" text-anchor="end">
      <tspan x="742" y="254" textLength="267" lengthAdjust="spacing">This chocolate will treat more</tspan>
      <tspan x="742" y="280" textLength="221" lengthAdjust="spacing">than just your tastebuds.</tspan>
      <tspan x="742" y="330" textLength="263" lengthAdjust="spacing">The fibre rich dark chocolate</tspan>
      <tspan x="742" y="356" textLength="252" lengthAdjust="spacing">will treat your figure aswell.</tspan>
    </text>
  </svg>

  <svg class="box-front box-front--white" viewBox="0 0 776 386" aria-label="White box front">
    <rect class="frame" width="776" height="386"/>
    <rect class="panel" x="3" y="3" width="770" height="380"/>
    <rect class="brand-block" x="3" y="4" width="405" height="177"/>
    <circle class="brand-dot" cx="44" cy="96" r="9"/>
    <text class="brand-name" x="64" y="107" textLength="310" lengthAdjust="spacing">OTAKEFERNUBRIO</text>
    <polygon class="flavour-tab--white" points="448,3 773,3 773,101 463,136"/>
    <text class="flavour-name flavour-name--dark" x="743" y="68" text-anchor="end" textLength="256" lengthAdjust="spacingAndGlyphs">White Box - Reward</text>
    <text class="copy" text-anchor="end">
      <tspan x="742" y="256" textLength="267" lengthAdjust="spacing">This chocolate will treat more</tspan>
      <tspan x="742" y="282" textLength="221" lengthAdjust="spacing">than just your tastebuds.</tspan>
      <tspan x="742" y="332" textLength="263" lengthAdjust="spacing">The fibre rich dark chocolate</tspan>
      <tspan x="742" y="358" textLength="252" lengthAdjust="spacing">will treat your figure aswell.</tspan>
    </text>
  </svg>

  <svg class="box-front box-front--milk" viewBox="0 0 776 386" aria-label="Milk box front">
    <rect class="frame" width="776" height="386"/>
    <rect class="panel" x="3" y="3" width="770" height="380"/>
    <rect class="brand-block" x="3" y="4" width="405" height="177"/>
    <circle class="brand-dot" cx="44" cy="96" r="9"/>
    <text class="brand-name" x="64" y="107" textLength="310" lengthAdjust="spacing">OTAKEFERNUBRIO</text>
    <polygon class="flavour-tab--milk" points="448,4 773,4 773,102 463,137"/>
    <text class="flavour-name flavour-name--light" x="740" y="68" text-anchor="end" textLength="248" lengthAdjust="spacing">Milk Box - Treat</text>
    <polygon class="weight-tab" points="3,267 355,229 371,383 3,383"/>
    <text class="net-weight" x="36" y="358" textLength="268" lengthAdjust="spacing">12 x 15.5g Chocolate Minibars</text>
    <text class="copy" text-anchor="end">
      <tspan x="742" y="256" textLength="267" lengthAdjust="spacing">This chocolate will treat more</tspan>
      <tspan x="742" y="282" textLength="221" lengthAdjust="spacing">than just your tastebuds.</tspan>
      <tspan x="742" y="332" textLength="263" lengthAdjust="spacing">The fibre rich dark chocolate</tspan>
      <tspan x="742" y="358" textLength="252" lengthAdjust="spacing">will treat your figure aswell.</tspan>
    </text>
  </svg>

</main>
</body>
</html>
```